To create a website for KWRB Accounting and Tax Services

I want to create a website that has a compelling and clean home page, social media connections, some about information, services, pricing and a spot to do simple time bookings and a contact page. I have attached a sample pricing chart, and designs of my logo, business card and letterhead. KWRB Accounting and Tax Services is a small business in beautiful Niagara on the Lake which offers bookkeeping and tax services to the local residents and businesses. I would like the winning design that use the black and blue colour scheme from my stationary and should communicate a professional business that people can trust.

Target Market(s)

local residents who need their taxes prepared as well as small business who need bookkeeping services

Industry/Entity Type

Bookkeeper

Coding

Coded - Design and coding required

Number of Pages Required

5+ page

Font styles to use
Sans Serif

Requirements
Must have
• clean home page with hero images, about section (can be on home page), separate page for services, pricing, time slot booking and contact, social media connections including facebook page, twitter, linkedin,

```html
<!DOCTYPE html>
<html lang="en">
<head>
<meta charset="utf-8">
<title>KWRB Accounting and Tax Services</title>
<link href="https://fonts.googleapis.com/css2?family=Raleway:wght@500;600;700;800&family=Source+Sans+3:wght@400;600;700&display=swap" rel="stylesheet">
<style>
:root{
  --blue:#1e8fd2;
  --black:#050505;
  --ink:#111;
  --grey-text:#666;
  --field:#f1f1f1;
  --band-grey:#e2e2e2;
  --white:#fff;
}
*{margin:0;padding:0;box-sizing:border-box}
html,body{width:1200px;height:2809px;overflow:hidden;background:var(--white)}
body{font-family:"Source Sans 3",Arial,sans-serif;color:var(--ink);position:relative}
.heading{font-family:"Raleway",Arial,sans-serif}
.wrap{width:878px;margin:0 auto;position:relative}
.section{position:relative;width:1200px;overflow:hidden}

/* top bar */
.topbar{height:37px}
.topbar svg.bg{position:absolute;inset:0}
.topbar .wrap{display:flex;justify-content:space-between;align-items:center;height:37px}
.social-top{display:flex;height:37px}
.social-top span{width:37px;height:37px;border-left:1px solid rgba(255,255,255,.25);display:flex;align-items:center;justify-content:center}
.social-top span:last-child{border-right:1px solid rgba(255,255,255,.25)}
.social-top span i{width:10px;height:10px;background:rgba(255,255,255,.85);display:block}
.top-phone{color:var(--white);font-weight:700;font-size:17px;display:flex;align-items:center;gap:8px}

/* header */
.header{height:83px;background:var(--white)}
.header .wrap{display:flex;justify-content:space-between;align-items:center;height:83px}
.brand{display:flex;align-items:center;gap:12px;font-family:"Raleway",sans-serif;font-weight:700;font-size:19px;color:var(--blue);letter-spacing:.5px}
.brand i{width:22px;height:22px;background:var(--blue);display:block}
.nav{display:flex;gap:25px;font-family:"Raleway",sans-serif;font-weight:600;font-size:12.5px;color:#333}
.nav .on{color:var(--blue)}

/* hero */
.hero{height:600px}
.hero .photo{position:absolute;inset:0;background:linear-gradient(120deg,#6f6f6d 0%,#8c8c88 45%,#767672 100%)}
.hero .shade{position:absolute;inset:0;background:rgba(20,20,20,.35)}
.hero-text{position:absolute;left:0;right:0;top:198px;text-align:center;color:var(--white)}
.hero-text .big{font-size:60px;font-weight:800;color:var(--blue);line-height:1}
.hero-text .sub{font-size:38px;font-weight:700;margin-top:6px}
.hero-text p{font-family:"Source Sans 3",sans-serif;font-size:13.5px;line-height:21px;width:640px;margin:14px auto 0}
.btns{display:flex;justify-content:center;gap:15px;margin-top:26px}
.btn{display:inline-block;font-family:"Raleway",sans-serif;font-weight:700;font-size:12px;padding:0 25px;height:44px;line-height:44px;letter-spacing:.2px}
.btn.solid{background:var(--blue);color:var(--white)}
.btn.light{background:var(--white);color:var(--blue)}
.btn.dark-text{background:var(--white);color:var(--ink)}

/* welcome */
.welcome{height:402px;text-align:center}
.welcome h2{padding-top:88px;font-size:34px;font-weight:800;line-height:44px}
.welcome h2 .b{color:var(--blue)}
.welcome p{font-size:12px;line-height:19.5px;color:var(--grey-text);width:700px;margin:30px auto 0}
.welcome .btn{margin-top:20px;height:41px;line-height:41px}

/* services */
.services{height:517px;text-align:center;color:var(--white)}
.services .photo{position:absolute;inset:0;background:linear-gradient(100deg,#3a3836 0%,#55514d 50%,#3d3a37 100%)}
.services .shade{position:absolute;inset:0;background:rgba(0,0,0,.35)}
.services h2{position:relative;padding-top:84px;font-size:33px;font-weight:800}
.services h2 .b{color:var(--blue)}
.services .lead{position:relative;font-size:12px;line-height:19.5px;width:660px;margin:4px auto 0}
.cards{position:relative;display:flex;gap:32px;margin-top:34px}
.card{width:195px;height:224px;background:var(--white);color:var(--ink);padding-top:42px;text-align:center}
.card .icon{display:block;margin:0 auto}
.card h3{font-family:"Raleway",sans-serif;font-weight:700;font-size:16.5px;margin-top:10px}
.card p{font-size:11.5px;line-height:19.5px;color:var(--grey-text);margin-top:4px;padding:0 10px}
.card .more{font-family:"Raleway",sans-serif;font-weight:700;font-size:11px;color:var(--blue);margin-top:8px;display:flex;justify-content:center;align-items:center;gap:5px}
.card .more svg{display:inline-block;margin:0}

/* pricing / booking band */
.band{height:180px}
.band svg.bg{position:absolute;inset:0}
.band-item{position:absolute;top:0;height:180px;display:flex;align-items:center}
.band-item .ico{width:80px;display:flex;justify-content:center}
.band-item .rule{width:1px;height:146px}
.band-item .txt{padding-left:24px}
.band-item h2{font-size:27px;font-weight:800}
.band-item p{font-size:12px;line-height:19.5px;width:300px;margin-top:2px}
.band-item .btn{margin-top:10px;height:41px;line-height:41px}
.pricing{left:135px;color:var(--white)}
.pricing .rule{background:rgba(255,255,255,.3)}
.booking{left:636px;color:var(--ink)}
.booking p{color:var(--grey-text)}
.booking .rule{background:var(--blue)}

/* contact */
.contact{height:457px;text-align:center}
.contact h2{padding-top:86px;font-size:34px;font-weight:800}
.contact h2 .b{color:var(--blue)}
.contact .lead{font-size:12px;line-height:19.5px;color:var(--grey-text);width:620px;margin:2px auto 0}
.form{display:flex;gap:8px;width:570px;margin:20px auto 0;text-align:left}
.form .col{display:flex;flex-direction:column;gap:8px}
.field{background:var(--field);font-size:12px;color:#555;padding:0 12px;height:37px;line-height:37px;width:263px}
.field.msg{width:299px;height:127px;line-height:1;padding-top:12px}
.contact .btn{margin-top:8px;height:41px;line-height:41px}

/* keep in touch */
.keep{height:495px}
.keep .photo{position:absolute;inset:0;background:linear-gradient(180deg,#4aa7dd 0%,#3c9dd6 60%,#2c8ccd 100%)}
.keep .box{position:absolute;left:395px;top:90px;width:411px;height:277px;background:rgba(255,255,255,.14)}
.keep h2{position:absolute;left:0;right:0;top:130px;text-align:center;font-size:34px;font-weight:800;color:#0a0a0a}
.kt{position:absolute;display:flex;align-items:center;gap:11px;font-size:11.5px;color:#0a0a0a;line-height:19px}
.kt .sq{width:33px;height:33px;background:var(--white);display:flex;align-items:center;justify-content:center;flex:none}
.kt.phone b{font-size:14px}
.keep .soc{position:absolute;top:309px;left:539px;display:flex;gap:12px}
.keep .soc span{width:33px;height:33px;border:1px solid var(--white);display:flex;align-items:center;justify-content:center}
.keep .soc span.fill{background:var(--white)}
.keep .soc span i{width:9px;height:9px;background:var(--blue);display:block}
.keep .soc span:not(.fill) i{background:var(--white)}

/* footer */
.footer{height:38px}
.footer svg.bg{position:absolute;inset:0}
.footer .wrap{display:flex;justify-content:space-between;align-items:center;height:38px;font-size:11.5px;color:var(--white)}
</style>
</head>
<body>

<div class="section topbar">
  <svg class="bg" width="1200" height="37" aria-hidden="true">
    <rect width="1200" height="37" fill="#050505"/>
    <polygon points="0,0 605,0 591,37 0,37" fill="#1e8fd2"/>
    <polygon points="605,0 612,0 598,37 591,37" fill="#fff"/>
  </svg>
  <div class="wrap">
    <div class="social-top" aria-label="Social profiles">
      <span aria-label="Social profile one"><i></i></span>
      <span aria-label="Social profile two"><i></i></span>
      <span aria-label="Social profile three"><i></i></span>
    </div>
    <div class="top-phone">
      <svg width="15" height="15" viewBox="0 0 24 24"><path fill="#fff" d="M6.6 10.8a15.1 15.1 0 0 0 6.6 6.6l2.2-2.2c.3-.3.7-.4 1-.2 1.1.4 2.3.6 3.6.6.6 0 1 .4 1 1V20c0 .6-.4 1-1 1A17 17 0 0 1 3 4c0-.6.4-1 1-1h3.5c.6 0 1 .4 1 1 0 1.3.2 2.5.6 3.6.1.3 0 .7-.2 1z"/></svg>
      905 555 0142
    </div>
  </div>
</div>

<header class="section header">
  <div class="wrap">
    <div class="brand"><i></i>KWRB Accounting and Tax Services</div>
    <nav class="nav">
      <span class="on">HOME</span><span>ABOUT</span><span>SERVICES</span><span>PRICING</span><span>BOOKING</span><span>CONTACT</span>
    </nav>
  </div>
</header>

<section class="section hero">
  <div class="photo" role="img" aria-label="Hands using a calculator and pen over financial reports and charts"></div>
  <div class="shade"></div>
  <div class="hero-text heading">
    <div class="big">KWRB</div>
    <div class="sub">ACCOUNTING AND TAX SERVICES</div>
    <p>Lorem Ipsum is simply dummy text of the printing and typesetting industry. Lorem Ipsum has been the industry's standard dummy text ever since the 1500s, when an unknown printer took a galley .</p>
    <div class="btns">
      <span class="btn solid">FREE CONSULTATION</span>
      <span class="btn light">BOOKING ONLINE</span>
    </div>
  </div>
</section>

<section class="section welcome">
  <h2 class="heading">WELCOME TO<br><span class="b">KWRB ACCOUNTING AND TAX SERVICES</span></h2>
  <p>Lorem Ipsum is simply dummy text of the printing and typesetting industry. Lorem Ipsum has been the industry's standard dummy text ever since the 1500s, when an unknown printer took a galley of type and scrambled it to make a type specimen book. It has survived not only five centuries, but also the leap into electronic typesetting, remaining essentially unchanged.</p>
  <span class="btn solid">READ &nbsp;MORE</span>
</section>

<section class="section services">
  <div class="photo" role="img" aria-label="Woman working at a desk with flowers in the background"></div>
  <div class="shade"></div>
  <h2 class="heading">OUR <span class="b">SERVICES</span></h2>
  <p class="lead">Lorem Ipsum is simply dummy text of the printing and typesetting industry. Lorem Ipsum has been the industry's standard dummy text ever since the 1500s, when an unknown printer took a galley of type and scrambled it to make a type specimen book.</p>
  <div class="wrap cards">
    <div class="card">
      <svg class="icon" width="40" height="44" viewBox="0 0 40 44" fill="none" stroke="#1e8fd2" stroke-width="1.6"><path d="M15 4h10l-3 7h-4z"/><path d="M18 11c-8 4-12 12-11 20 1 6 6 8 13 8s12-2 13-8c1-8-3-16-11-20"/><text x="14" y="31" font-size="13" fill="#1e8fd2" stroke="none" font-family="Arial">$</text><text x="26" y="40" font-size="9" fill="#1e8fd2" stroke="none" font-family="Arial">%</text></svg>
      <h3>Income Tax</h3>
      <p>Lorem Ipsum is dummy text of the printing and typesetting industry.</p>
      <div class="more">READ MORE <svg width="16" height="8"><path d="M0 4h14M10 1l4 3-4 3" stroke="#1e8fd2" fill="none"/></svg></div>
    </div>
    <div class="card">
      <svg class="icon" width="46" height="44" viewBox="0 0 46 44" fill="none" stroke="#1e8fd2" stroke-width="1.6"><rect x="8" y="2" width="26" height="36"/><path d="M13 9h16M13 14h10"/><circle cx="26" cy="22" r="5"/><rect x="2" y="24" width="12" height="18"/><path d="M5 29h6M5 34h6"/><path d="M40 6l3 3-9 18-3-3z"/></svg>
      <h3>Financial Audit</h3>
      <p>Lorem Ipsum is dummy text of the printing and typesetting industry.</p>
      <div class="more">READ MORE <svg width="16" height="8"><path d="M0 4h14M10 1l4 3-4 3" stroke="#1e8fd2" fill="none"/></svg></div>
    </div>
    <div class="card">
      <svg class="icon" width="46" height="44" viewBox="0 0 46 44" fill="none" stroke="#1e8fd2" stroke-width="1.6"><circle cx="20" cy="10" r="8"/><text x="16" y="15" font-size="12" fill="#1e8fd2" stroke="none" font-family="Arial">$</text><path d="M30 8h12M30 13h9"/><rect x="6" y="28" width="6" height="14"/><rect x="15" y="22" width="6" height="20"/><rect x="24" y="26" width="6" height="16"/><path d="M2 42h40"/></svg>
      <h3>Outsourced CFO</h3>
      <p>Lorem Ipsum is dummy text of the printing and typesetting industry.</p>
      <div class="more">READ MORE <svg width="16" height="8"><path d="M0 4h14M10 1l4 3-4 3" stroke="#1e8fd2" fill="none"/></svg></div>
    </div>
    <div class="card">
      <svg class="icon" width="42" height="44" viewBox="0 0 42 44" fill="none" stroke="#1e8fd2" stroke-width="1.6"><rect x="16" y="10" width="10" height="32"/><path d="M21 2v8M18 6h6"/><rect x="4" y="22" width="12" height="20"/><rect x="26" y="26" width="11" height="16"/><path d="M8 28h4M8 34h4M20 16h2M20 22h2M20 28h2M30 32h3M1 42h40"/></svg>
      <h3>Business valuation</h3>
      <p>Lorem Ipsum is dummy text of the printing and typesetting industry.</p>
      <div class="more">READ MORE <svg width="16" height="8"><path d="M0 4h14M10 1l4 3-4 3" stroke="#1e8fd2" fill="none"/></svg></div>
    </div>
  </div>
</section>

<section class="section band">
  <svg class="bg" width="1200" height="180" aria-hidden="true">
    <rect width="1200" height="180" fill="#e2e2e2"/>
    <polygon points="0,0 580,0 617,90 580,180 0,180" fill="#1e8fd2"/>
    <polyline points="586,0 623,90 586,180" stroke="#fff" stroke-width="6" fill="none"/>
  </svg>
  <div class="band-item pricing">
    <div class="ico"><svg width="36" height="64" viewBox="0 0 36 64"><text x="0" y="56" font-size="72" font-weight="700" fill="#fff" font-family="Arial">$</text></svg></div>
    <div class="rule"></div>
    <div class="txt">
      <h2 class="heading">PRICING</h2>
      <p>Lorem Ipsum is simply dummy text of the printing and typesetting industry. Lorem Ipsum has been the industry.</p>
      <span class="btn dark-text">SELECT YOUR PLAN</span>
    </div>
  </div>
  <div class="band-item booking">
    <div class="ico"><svg width="60" height="62" viewBox="0 0 60 62" fill="none" stroke="#1e8fd2" stroke-width="2.6"><rect x="3" y="8" width="54" height="51" rx="4"/><path d="M3 20h54M16 2v12M44 2v12"/><g fill="#1e8fd2" stroke="none"><rect x="15" y="28" width="6" height="5"/><rect x="27" y="28" width="6" height="5"/><rect x="39" y="28" width="6" height="5"/><rect x="15" y="38" width="6" height="5"/><rect x="27" y="38" width="6" height="5"/><rect x="39" y="38" width="6" height="5"/><rect x="15" y="48" width="6" height="5"/><rect x="27" y="48" width="6" height="5"/></g></svg></div>
    <div class="rule"></div>
    <div class="txt">
      <h2 class="heading">BOOKING</h2>
      <p>Lorem Ipsum is simply dummy text of the printing and typesetting industry. Lorem Ipsum has been the industry.</p>
      <span class="btn solid">REQUEST YOUR BOOK</span>
    </div>
  </div>
</section>

<section class="section contact">
  <h2 class="heading">GET IN TOUCH <span class="b">WITH US</span></h2>
  <p class="lead">Lorem Ipsum is simply dummy text of the printing and typesetting industry. Lorem Ipsum has been the industry's standard dummy text ever since the 1500s, when an unknown printer took a galley.</p>
  <div class="form">
    <div class="col">
      <div class="field">Enter Name</div>
      <div class="field">Enter Email</div>
      <div class="field">Enter Contact No.</div>
    </div>
    <div class="field msg">Enter Message</div>
  </div>
  <span class="btn solid">REQUEST FREE CONSULTATION</span>
</section>

<section class="section keep">
  <div class="photo" role="img" aria-label="Lakeside gazebo in winter, tinted blue"></div>
  <div class="box"></div>
  <h2 class="heading">KEEP IN TOUCH</h2>
  <div class="kt phone" style="left:416px;top:182px">
    <span class="sq"><svg width="14" height="14" viewBox="0 0 24 24"><path fill="#1e8fd2" d="M6.6 10.8a15.1 15.1 0 0 0 6.6 6.6l2.2-2.2c.3-.3.7-.4 1-.2 1.1.4 2.3.6 3.6.6.6 0 1 .4 1 1V20c0 .6-.4 1-1 1A17 17 0 0 1 3 4c0-.6.4-1 1-1h3.5c.6 0 1 .4 1 1 0 1.3.2 2.5.6 3.6.1.3 0 .7-.2 1z"/></svg></span>
    <b>905 555 0142</b>
  </div>
  <div class="kt" style="left:588px;top:182px">
    <span class="sq"><svg width="14" height="11" viewBox="0 0 14 11"><rect width="14" height="11" fill="#1e8fd2"/><path d="M0 0l7 6 7-6" stroke="#fff" fill="none"/></svg></span>
    hello@kwrbaccounting.ca
  </div>
  <div class="kt" style="left:416px;top:236px">
    <span class="sq"><svg width="12" height="16" viewBox="0 0 12 16"><path d="M6 0a6 6 0 0 1 6 6c0 4-6 10-6 10S0 10 0 6a6 6 0 0 1 6-6z" fill="#1e8fd2"/><circle cx="6" cy="6" r="2.2" fill="#fff"/></svg></span>
    <span>218 Orchard Lane, Suite 12 P.O. Box 440<br>Lakeview Harbour, ON L0R 2K0</span>
  </div>
  <div class="soc" aria-label="Social profiles">
    <span class="fill" aria-label="Social profile one"><i></i></span>
    <span aria-label="Social profile two"><i></i></span>
    <span aria-label="Social profile three"><i></i></span>
  </div>
</section>

<footer class="section footer">
  <svg class="bg" width="1200" height="38" aria-hidden="true">
    <rect width="1200" height="38" fill="#050505"/>
    <polygon points="0,0 604,0 591,38 0,38" fill="#1e8fd2"/>
    <polygon points="604,0 611,0 598,38 591,38" fill="#fff"/>
  </svg>
  <div class="wrap">
    <span>© KWRB ACCOUNTING - 2019. All Rights Reserved.</span>
    <span>Privacy Policy &nbsp;| &nbsp;Terms &amp; Condition</span>
  </div>
</footer>

</body>
</html>
```